Business Card Design

Hoping for a black background business card, minimalistic design.
With the Copper Lantern logo you created in white.

I would like to include:
My Name and title
Address (street address)
Reception: (phone number)
Fax: (fax number)
Reception: (email address)
Direct email: (email address)
Instagram: (ig handle)

```html
<!DOCTYPE html>
<html lang="en">
<head>
<meta charset="utf-8">
<title>Copper Lantern — Business Card</title>
<link rel="stylesheet" href="https://fonts.googleapis.com/css2?family=Poppins:wght@400;500;600&display=swap">
<style>
  :root {
    --stage: #2a2a2a;
    --card-white: #ffffff;
    --card-black: #151515;
    --ink: #111111;
    --rule: #9a9a9a;
    --paper-text: #ffffff;
  }
  * { box-sizing: border-box; margin: 0; padding: 0; }
  html, body { width: 1200px; height: 1108px; overflow: hidden; }
  body {
    background: var(--stage);
    font-family: "Poppins", sans-serif;
    position: relative;
  }
  .card {
    position: absolute;
    top: 274px;
    width: 340px;
    height: 560px;
    border-radius: 18px;
  }
  .card-front {
    left: 220px;
    background: var(--card-white);
    color: var(--ink);
    text-align: center;
    padding-top: 52px;
  }
  .brand-mark {
    width: 98px; height: 98px;
    margin: 0 auto;
    border: 6px solid var(--ink);
    border-radius: 50%;
  }
  .brand-name {
    margin-top: 20px;
    font-size: 27px;
    font-weight: 500;
    letter-spacing: 4px;
    text-transform: uppercase;
  }
  .holder-name {
    margin-top: 38px;
    font-size: 19px;
    font-weight: 600;
    letter-spacing: 1px;
    text-transform: uppercase;
    line-height: 1.1;
  }
  .holder-title { font-size: 15px; line-height: 1.2; }
  .icon-row {
    display: flex; align-items: center; justify-content: center;
    gap: 5px; margin: 10px 28px 6px;
  }
  .icon-row .rule { flex: 1; height: 1px; background: var(--rule); }
  .icon-row svg { width: 24px; height: 24px; }
  .contact-lines { font-size: 14.5px; line-height: 1.3; }
  .divider { height: 1px; background: var(--rule); margin: 8px 44px; }
  .social { display: flex; align-items: center; justify-content: center; gap: 8px; font-size: 15px; }
  .social-box { width: 16px; height: 16px; border: 2px solid var(--ink); border-radius: 4px; }
  .card-back {
    left: 640px;
    background: var(--card-black);
    overflow: hidden;
  }
  .back-field {
    position: absolute; inset: 0;
    background: linear-gradient(135deg, #1c1c1c 0%, #121212 60%, #181818 100%);
  }
  .back-mark {
    position: absolute; left: 214px; top: 360px;
    display: flex; flex-direction: column; align-items: center; gap: 6px;
    color: var(--paper-text);
  }
  .back-mark-circle {
    width: 50px; height: 50px;
    border: 3px solid var(--paper-text); border-radius: 50%;
  }
  .back-mark-name { font-size: 9px; font-weight: 500; letter-spacing: 1.5px; text-transform: uppercase; }
</style>
</head>
<body>
  <section class="card card-front">
    <div class="brand-mark"></div>
    <div class="brand-name">Copper Lantern</div>
    <div class="holder-name">Daniel Reyes</div>
    <div class="holder-title">Managing Director</div>
    <div class="icon-row">
      <span class="rule"></span>
      <svg viewBox="0 0 24 24" aria-label="phone"><rect width="24" height="24" rx="4" fill="#111"/><path d="M7 6h3l1 3-2 1a8 8 0 0 0 4 4l1-2 3 1v3a1 1 0 0 1-1 1A11 11 0 0 1 6 7a1 1 0 0 1 1-1z" fill="#fff"/></svg>
      <svg viewBox="0 0 24 24" aria-label="fax"><rect width="24" height="24" rx="4" fill="#111"/><rect x="8" y="5" width="8" height="5" fill="#fff"/><rect x="5" y="10" width="14" height="6" rx="1" fill="#fff"/><rect x="8" y="14" width="8" height="5" fill="#fff" stroke="#111"/></svg>
      <svg viewBox="0 0 24 24" aria-label="email"><rect width="24" height="24" rx="4" fill="#111"/><rect x="5" y="7" width="14" height="10" fill="#fff"/><path d="M5 7l7 6 7-6M5 17l5-5M19 17l-5-5" stroke="#111" fill="none"/></svg>
      <svg viewBox="0 0 24 24" aria-label="email"><rect width="24" height="24" rx="4" fill="#111"/><rect x="5" y="7" width="14" height="10" fill="#fff"/><path d="M5 7l7 6 7-6M5 17l5-5M19 17l-5-5" stroke="#111" fill="none"/></svg>
      <span class="rule"></span>
    </div>
    <div class="contact-lines">
      <p>055-210 338 417</p>
      <p>055-210 338 417</p>
      <p>hello@copperlantern.co (Reception)</p>
      <p>hello@copperlantern.co(Direct)</p>
    </div>
    <div class="divider"></div>
    <div class="contact-lines">
      <p>421, Address line goes here</p>
      <p>45452,Country Name</p>
    </div>
    <div class="divider"></div>
    <div class="social"><span class="social-box"></span><span>ig handle</span></div>
  </section>

  <section class="card card-back">
    <div class="back-field" role="img" aria-label="Subtle tone-on-tone repeated brand pattern on black"></div>
    <div class="back-mark">
      <span class="back-mark-circle"></span>
      <span class="back-mark-name">Copper Lantern</span>
    </div>
  </section>
</body>
</html>
```